Peaks4You LOGO + Business Card design for a Ski Tour agency

- New start-up international tour agency focused on skiing tours
- Connected with the Alps
- Targeted at Asians
- Business/Brand name: Peaks4You

```html
<!DOCTYPE html>
<html lang="en">
<head>
<meta charset="UTF-8">
<title>Peaks4You Business Card</title>
<link href="https://fonts.googleapis.com/css2?family=Arimo:wght@400;700&display=swap" rel="stylesheet">
<style>
  :root {
    --page-bg: #d9d3cb;
    --card-bg: #f3efec;
    --ink: #3b3b3d;
    --ink-soft: #4a4a4c;
    --brand-red: #9e1b22;
    --band-red: #8c141b;
    --band-dark: #4a4a4c;
    --on-red: #f4e6e6;
  }
  html, body {
    margin: 0;
    padding: 0;
    width: 1200px;
    height: 970px;
    overflow: hidden;
    background: var(--page-bg);
    font-family: "Arimo", Arial, sans-serif;
  }
  .business-card {
    position: absolute;
    left: 80px;
    top: 188px;
    width: 1040px;
    height: 594px;
    border-radius: 26px;
    background: linear-gradient(160deg, #f7f4f2 0%, var(--card-bg) 55%, #ebe6e2 100%);
    box-shadow: 0 18px 40px rgba(60, 45, 35, 0.25);
    overflow: hidden;
  }
  .brand-name {
    position: absolute;
    left: 55px;
    top: 244px;
    margin: 0;
    font-size: 64px;
    font-weight: 400;
    letter-spacing: 2px;
    color: var(--ink);
    line-height: 1;
  }
  .person-name {
    position: absolute;
    left: 55px;
    top: 394px;
    margin: 0;
    font-size: 33px;
    font-weight: 700;
    color: var(--ink);
    line-height: 1;
  }
  .person-role {
    position: absolute;
    left: 55px;
    top: 425px;
    margin: 0;
    font-size: 25px;
    color: var(--brand-red);
    line-height: 1;
  }
  .divider-line {
    position: absolute;
    left: 155px;
    top: 444px;
    width: 830px;
    height: 2px;
    background: var(--brand-red);
  }
  .contact-list {
    position: absolute;
    left: 55px;
    top: 468px;
    margin: 0;
    padding: 0;
    list-style: none;
  }
  .contact-item {
    display: flex;
    align-items: center;
    height: 40px;
    font-size: 27px;
    color: var(--ink-soft);
  }
  .contact-icon {
    width: 36px;
    height: 36px;
    margin-right: 14px;
    flex: none;
  }
  .postal-address {
    position: absolute;
    right: 55px;
    top: 472px;
    margin: 0;
    font-style: normal;
    font-size: 25px;
    line-height: 38px;
    color: var(--ink);
  }
  .footer-bands {
    position: absolute;
    left: 0;
    bottom: 0;
    width: 1040px;
    height: 48px;
  }
  .website {
    position: absolute;
    right: 58px;
    top: 558px;
    margin: 0;
    font-size: 23px;
    color: var(--on-red);
    line-height: 1;
  }
</style>
</head>
<body>
  <main class="business-card">
    <h1 class="brand-name">Peaks4You</h1>

    <p class="person-name">DANIEL REED</p>
    <p class="person-role">Owner</p>
    <div class="divider-line"></div>

    <ul class="contact-list">
      <li class="contact-item">
        <svg class="contact-icon" viewBox="0 0 36 36" aria-hidden="true">
          <circle cx="18" cy="18" r="18" fill="var(--brand-red)"/>
          <rect x="12" y="8" width="12" height="20" rx="2.5" fill="none" stroke="#fff" stroke-width="2"/>
          <line x1="16" y1="24.5" x2="20" y2="24.5" stroke="#fff" stroke-width="1.6"/>
        </svg>
        555.010.2468
      </li>
      <li class="contact-item">
        <svg class="contact-icon" viewBox="0 0 36 36" aria-hidden="true">
          <circle cx="18" cy="18" r="18" fill="var(--brand-red)"/>
          <rect x="9" y="11" width="18" height="13" fill="none" stroke="#fff" stroke-width="1.8"/>
          <polyline points="9,11 18,19 27,11" fill="none" stroke="#fff" stroke-width="1.8"/>
          <line x1="9" y1="24" x2="15.5" y2="17" stroke="#fff" stroke-width="1.5"/>
          <line x1="27" y1="24" x2="20.5" y2="17" stroke="#fff" stroke-width="1.5"/>
        </svg>
        hello@peaks4youmail.com
      </li>
    </ul>

    <address class="postal-address">
      PO BOX 456, Ridge Road<br>
      3rd Lane, Alpine Vale 67890
    </address>

    <svg class="footer-bands" viewBox="0 0 1040 48" preserveAspectRatio="none" aria-hidden="true">
      <polygon points="0,28 600,28 593,48 0,48" fill="var(--band-dark)"/>
      <polygon points="618,0 1040,0 1040,48 604,48" fill="var(--band-red)"/>
    </svg>
    <p class="website">www.peaks4youtours.com</p>
  </main>
</body>
</html>
```